Medical Device Packaging Project 1 of 5

We are a medical device startup company needing packaging for a total of 5 device brands. This is posting 1 of 5 and the device name is "Vexomira"

Vexomira is an intraocular lens for use in cataract surgery. The target market is Chinese ophthalmologists. The box should be sophisticated and upmarket.

The company name is Tambrel Vision, I have included the logo in the uploaded files section. You should include the logo on the box.

I have uploaded a sample lens boxes from other companies that demonstrate the information needed to be contained on the box in terms of address, warnings, symbols, etc.

I have also uploaded the blank dieline of the boxes

You are welcome and encouraged to also submit to projects 2, 3, 4, and 5 as well. The same rules and expectations apply.

Industry/Entity Type

It Company

Requirements
Should not have
• Should not have any images of an eye or any bionic/futuristic feel to the design
• Note that the quindaret box is for text reference only. You may use the lens image but the futuristic/bionic look is NOT what we are going for with this brand. It should be traditional upmarket medical device artwork.

```html
<!DOCTYPE html>
<html lang="en">
<head>
<meta charset="utf-8">
<title>Vexomira – Hydrophobic Intraocular Lens Box Panels</title>
<link rel="stylesheet" href="https://fonts.googleapis.com/css2?family=Arimo:wght@400&family=Montserrat:wght@500;600;700&display=swap">
<style>
  :root {
    --stage: #ececec;
    --navy: #1d3f78;
    --ink: #1f3157;
    --wash-light: #f5fafd;
    --wash-mid: #d3ebf7;
    --wash-deep: #a3d5ef;
    --mark-ring: #9cc6e2;
    --lens-silver: #b9bcc0;
    --lens-dark: #7a7e84;
  }
  * { margin: 0; padding: 0; box-sizing: border-box; }
  html, body {
    width: 1200px;
    height: 782px;
    overflow: hidden;
    background: var(--stage);
    font-family: "Montserrat", sans-serif;
  }
  .panel {
    position: absolute;
    top: 150px;
    width: 560px;
    height: 480px;
    overflow: hidden;
    background: var(--wash-light);
    box-shadow: 0 8px 24px rgba(0,0,0,0.12);
  }
  .panel-back { left: 25px; }
  .panel-front { left: 615px; }
  .watercolor-wash {
    position: absolute;
    inset: 0;
    background:
      radial-gradient(ellipse 70% 40% at 40% 72%, var(--wash-deep) 0%, rgba(163,213,239,0) 70%),
      radial-gradient(ellipse 55% 35% at 85% 50%, var(--wash-mid) 0%, rgba(211,235,247,0) 70%),
      linear-gradient(180deg, var(--wash-light) 0%, var(--wash-mid) 55%, var(--wash-deep) 100%);
  }
  .brand {
    position: absolute;
    left: 34px;
    top: 96px;
    display: flex;
    align-items: center;
    gap: 9px;
  }
  .brand-dot {
    width: 14px;
    height: 14px;
    border-radius: 50%;
    background: var(--mark-ring);
  }
  .brand-name {
    font-weight: 600;
    font-size: 19px;
    letter-spacing: 0.05em;
    color: var(--navy);
    text-transform: uppercase;
  }
  .device-type {
    position: absolute;
    right: 26px;
    top: 60px;
    font-weight: 600;
    font-size: 14.5px;
    line-height: 1.35;
    letter-spacing: 0.02em;
    color: var(--navy);
    text-align: right;
  }
  .lens-visual {
    position: absolute;
    border-radius: 50%;
    background: radial-gradient(circle at 45% 40%, #f4f5f6 0%, var(--lens-silver) 45%, var(--lens-dark) 100%);
    opacity: 0.85;
  }
  .panel-back .lens-visual { left: 360px; top: 175px; width: 130px; height: 150px; }
  .panel-front .lens-visual { left: 330px; top: 150px; width: 190px; height: 230px; }
  .warnings {
    position: absolute;
    left: 34px;
    top: 176px;
    font-family: "Arimo", sans-serif;
    font-size: 8.4px;
    line-height: 10px;
    color: var(--ink);
  }
  .warnings p + p { margin-top: 5px; }
  .symbols {
    position: absolute;
    right: 26px;
    bottom: 58px;
  }
  .product {
    position: absolute;
    left: 34px;
    bottom: 48px;
    color: var(--navy);
  }
  .product-name {
    font-weight: 700;
    font-size: 26px;
    letter-spacing: 0.14em;
    text-transform: uppercase;
  }
  .product-spec {
    font-weight: 600;
    font-size: 16px;
    letter-spacing: 0.02em;
    margin-top: 2px;
  }
</style>
</head>
<body>
  <section class="panel panel-back">
    <div class="watercolor-wash" role="img" aria-label="Soft blue watercolour wash background"></div>
    <div class="brand">
      <span class="brand-dot"></span>
      <span class="brand-name">Tambrel Vision</span>
    </div>
    <h2 class="device-type">HYDROPHOBIC INTRAOCULAR LENS<br>ASPHERIC WITH 360° LENS</h2>
    <div class="lens-visual" role="img" aria-label="Illustration of an intraocular lens with curved haptics"></div>
    <div class="warnings">
      <p>Contains one sterile intraocular lens<br>Do not use if the packaging is damaged<br>Do not resterilize</p>
      <p>Bevat één steriele intraoculaire lens<br>Niet gebruiken als de verpakking beschadigd is<br>Niet opnieuw steriliseren</p>
      <p>Contient une lentille intraoculaire stérile<br>Ne pas utiliser si l'emballage est endommagé<br>Ne pas restériliser</p>
      <p>Enthält eine sterile intraokulare Linse<br>Nicht verwenden, wenn die Verpackung beschädigt ist<br>Nicht resterilisieren</p>
      <p>Periéchei éna aposteiroméno endofthálmio fakó OR<br>Περιέχει ένα αποστειρωμένο ενδοφθάλμιο φακό<br>Μην το χρησιμοποιείτε εάν η συσκευασία έχει υποστεί ζημιά<br>OR Mín to chrisimopoieíte eán i syskevasía échei ypostei zimiá<br>Μην επαναποστειρώνετε OR Mín epanaposteirónete</p>
      <p>Contiene una lente intraoculare sterile<br>Non usare se la confezione è danneggiata<br>Non risterilizzare</p>
      <p>Contém uma lente intra-ocular esterilizada<br>Não use se a embalagem está danificada<br>Não reesterilize</p>
      <p>Contiene una lente intraocular estéril<br>No utilizar si el envase está dañado<br>No vuelva a esterilizar</p>
    </div>
    <svg class="symbols" width="150" height="22" viewBox="0 0 150 22" aria-label="Regulatory symbols">
      <g fill="none" stroke="#1f3157" stroke-width="1">
        <rect x="0.5" y="4.5" width="40" height="13"/>
        <line x1="28.5" y1="4.5" x2="28.5" y2="17.5"/>
        <path d="M60 5 L68 18 L52 18 Z"/>
        <line x1="60" y1="9" x2="60" y2="14"/>
        <circle cx="85" cy="11" r="7"/>
        <line x1="80" y1="16" x2="90" y2="6"/>
        <circle cx="108" cy="11" r="7"/>
        <line x1="103" y1="16" x2="113" y2="6"/>
        <circle cx="131" cy="11" r="7"/>
        <line x1="126" y1="16" x2="136" y2="6"/>
      </g>
      <g fill="#1f3157" font-family="Arimo, sans-serif" font-size="6.5">
        <text x="3" y="13.5">STERILE</text>
        <text x="30.5" y="13.5">EO</text>
      </g>
    </svg>
  </section>

  <main class="panel panel-front">
    <div class="watercolor-wash" role="img" aria-label="Soft blue watercolour wash background"></div>
    <div class="brand">
      <span class="brand-dot"></span>
      <span class="brand-name">Tambrel Vision</span>
    </div>
    <h1 class="device-type">HYDROPHOBIC INTRAOCULAR LENS</h1>
    <div class="lens-visual" role="img" aria-label="Illustration of an intraocular lens with curved haptics"></div>
    <div class="product">
      <div class="product-name">Vexomira</div>
      <div class="product-spec">ASPHERIC WITH 360° LENS</div>
    </div>
  </main>
</body>
</html>
```